Infographic for a Christian church discipleship pathway

We need to take a fairly complex program that helps people in a Baptist church follow Jesus, and turn it into a simple graphic. This graphic does not have to explain the whole program, web pages and print materials will do that. But, it should be something that people see and understand what it is quickly. The attached graphic is only to give the key words and general direction of the program. It should not serve as a design guide. In other words, we want to see some other ideas how this information can be imparted graphically with concision and creativity. It's important to note, the categories at the top (pray daily, read daily, gather weekly) are first steps, starting points....one shouldn't move forward until they've incorporated these things into their life. However, the categories that follow (study, connect, serve, etc) are not necessarily steps to take in sequential order.

The diagrams we've provided are not what we expect. They are only to explain the program. Here is a verbal description: The motto of our church is "A Ready Church" (ready to serve, ready to love, ready for when Jesus returns). There are four words that describe a ready church member: FOCUSED on the return of Christ, FAITHFUL in a daily relationship with Jesus, PREPARED for any opportunity to be a supernatural vessel of God's worK, LOOKING to invite others into God's family. The first two are God's Work in Me (Focused and faithful); the second two are God's Work Through me (Prepared, looking). Please use those two things as you wish (Focused faithful prepared looking; and God's word in and through me). If they are clarifying, please use. If not, you don't have to use.

Additionally, the strategies we employ to be "a ready church" are 1. Prayer 2. God's Word, and 3. Biblical Community. (So, in other words, these three things help us be a people who is focused, faithful, prepared, and looking....which is a ready church.

To provide some information how we will build this out: this graphic will be used in print and digital content. The digital content will allow people to click on each category to access training and resources associated with that discipline. (Fasting, reflecting, etc).

www.kwm.parish

Target Market(s)

35-50

Industry/Entity Type

Religious

Other font styles liked:
• Lato and/or Cambria

Requirements
Must have
• Fonts: lato, cambria. Colors#: 373E41, ebebe8, #a69677. Accent Colors: 80401D, #4e5730, #a5bac8
Nice to have
• A designer who has an understanding of what it means to incorporate the spiritual disciplines of the Christian faith into their life.

```html
<!DOCTYPE html>
<html lang="en">
<head>
<meta charset="utf-8">
<title>The Ready Way</title>
<link rel="stylesheet" href="https://fonts.googleapis.com/css2?family=Lato:wght@400;700;900&display=swap">
<style>
  :root {
    --ink: #373e41;
    --mist: #ebebe8;
    --gold: #a69677;
    --sky: #a5bac8;
    --white: #ffffff;
  }
  * { margin: 0; padding: 0; box-sizing: border-box; }
  html, body { width: 1200px; height: 1063px; overflow: hidden; }
  body {
    font-family: "Lato", sans-serif;
    color: var(--ink);
    background: var(--white);
  }
  .poster {
    position: relative;
    width: 1200px;
    height: 1063px;
    overflow: hidden;
    background:
      linear-gradient(180deg, rgba(255,255,255,0) 78%, var(--white) 94%),
      radial-gradient(ellipse at 42% 0%, var(--white) 0%, #f3f3f1 40%, #d9d9d6 100%);
  }
  .sky-scene {
    position: absolute;
    left: 0; top: 0;
    width: 1200px; height: 1063px;
    background:
      repeating-conic-gradient(from 170deg at 44% -5%, rgba(255,255,255,0.35) 0deg 4deg, rgba(255,255,255,0) 4deg 9deg);
    opacity: 0.7;
  }
  .cloud-bank {
    position: absolute;
    left: 0; bottom: 0;
    width: 1200px; height: 210px;
    background: linear-gradient(180deg, rgba(255,255,255,0) 0%, var(--white) 55%);
  }
  .steeple {
    position: absolute;
    left: 131px; top: 244px;
    width: 131px; height: 731px;
    background: linear-gradient(180deg, var(--ink) 0%, var(--ink) 28%, #f4f4f2 30%, #ecedee 100%);
  }
  .title {
    position: absolute;
    left: 112px; top: 98px;
    font-weight: 900;
    font-size: 62px;
    letter-spacing: 1px;
    color: var(--ink);
  }
  .subtitle {
    position: absolute;
    left: 113px; top: 188px;
    font-size: 19px;
    letter-spacing: 2.2px;
    color: var(--gold);
    text-transform: uppercase;
  }
  .brand {
    position: absolute;
    left: 850px; top: 90px;
    display: flex;
    align-items: center;
    gap: 16px;
  }
  .brand-mark {
    width: 30px; height: 30px;
    background: var(--ink);
  }
  .brand-name {
    font-weight: 700;
    font-size: 25px;
    line-height: 1.12;
    text-transform: uppercase;
    color: var(--ink);
  }
  .pathway {
    position: absolute;
    left: 0; top: 0;
    width: 1200px; height: 1063px;
  }
  .pathway text { font-family: "Lato", sans-serif; dominant-baseline: central; text-anchor: middle; }
  .chevron-gold { fill: var(--gold); }
  .chevron-dark { fill: var(--ink); }
  .track { fill: rgba(255,255,255,0.55); stroke: var(--gold); stroke-width: 2; }
  .label-strategy { fill: var(--white); font-weight: 900; font-size: 21px; }
  .label-daily { fill: var(--white); font-size: 21px; }
  .label-practice { fill: var(--ink); font-size: 21px; }
</style>
</head>
<body>
<main class="poster">
  <div class="sky-scene" role="img" aria-label="Soft beams of light streaming through a pale cloudy sky"></div>
  <div class="steeple" role="img" aria-label="Illustration of a white church steeple with a dark spire and cross"></div>
  <div class="cloud-bank" role="img" aria-label="Soft white clouds along the bottom"></div>

  <h1 class="title">THE READY WAY</h1>
  <p class="subtitle">Rhythms &amp; Practices for a Ready Life</p>

  <div class="brand">
    <span class="brand-mark"></span>
    <span class="brand-name">Kingsway<br>Parish</span>
  </div>

  <svg class="pathway" viewBox="0 0 1200 1063" aria-label="Discipleship pathway">
    <g class="row row-prayer">
      <polygon class="track" points="500,450 1105,450 1129,487.5 1105,525 500,525"/>
      <polygon class="chevron-gold" points="71,450 281,450 306,487.5 281,525 71,525 96,487.5"/>
      <polygon class="chevron-dark" points="281,450 494,450 519,487.5 494,525 281,525 306,487.5"/>
      <text class="label-strategy" x="190" y="488">PRAYER</text>
      <text class="label-daily" x="401" y="488">Prayer Daily</text>
      <text class="label-practice" x="608" y="488">Rest</text>
      <text class="label-practice" x="735" y="488">Reflect</text>
      <text class="label-practice" x="862" y="488">Fast</text>
      <text class="label-practice" x="1009" y="488">Intercede</text>
    </g>
    <g class="row row-word">
      <polygon class="track" points="500,613 1105,613 1129,650.5 1105,688 500,688"/>
      <polygon class="chevron-gold" points="71,613 281,613 306,650.5 281,688 71,688 96,650.5"/>
      <polygon class="chevron-dark" points="281,613 494,613 519,650.5 494,688 281,688 306,650.5"/>
      <text class="label-strategy" x="190" y="651">WORD</text>
      <text class="label-daily" x="401" y="651">Word Daily</text>
      <text class="label-practice" x="608" y="651">Study</text>
      <text class="label-practice" x="735" y="651">Memorize</text>
      <text class="label-practice" x="862" y="651">Teach</text>
      <text class="label-practice" x="1009" y="651">Proclaim</text>
    </g>
    <g class="row row-community">
      <polygon class="track" points="500,776 1105,776 1129,813.5 1105,851 500,851"/>
      <polygon class="chevron-gold" points="71,776 281,776 306,813.5 281,851 71,851 96,813.5"/>
      <polygon class="chevron-dark" points="281,776 494,776 519,813.5 494,851 281,851 306,813.5"/>
      <text class="label-strategy" x="190" y="814">COMMUNITY</text>
      <text class="label-daily" x="401" y="814">Community Daily</text>
      <text class="label-practice" x="608" y="814">Connect</text>
      <text class="label-practice" x="735" y="814">Learn</text>
      <text class="label-practice" x="862" y="814">Give</text>
      <text class="label-practice" x="979" y="814">Serve</text>
    </g>
  </svg>
</main>
</body>
</html>
```